Pellrow Strategies business card

I need a business card for my new strategic consulting LLC, Pellrow Strategies. We specialize in helping people who care about broadband technology and telecommunications policy, and we're based in Washington DC. I'm looking for a card that says smart, credible, future-facing and signals a high level of expertise. It's DC, so there's clearly a limit to how crazy we can go with this card, but I am looking for a design that reflects a company that is comfortable with technology, policy, and having a little bit fun. I'm uploading my logo below, and I'd like to have it be part of the card design in some fashion.
Target Market(s)
Telecommunications and technology policy professionals
Industry/Entity Type
Technology policy
Contact Information for Business Card
Name of business, my name (Colin Mabberly), email (colin@pellrowstrategies.example) , phone number (202-555-0148)phone number
Look and feel

```html
<!DOCTYPE html>
<html lang="en">
<head>
<meta charset="utf-8">
<title>Pellrow Strategies — Business Card</title>
<link rel="stylesheet" href="https://fonts.googleapis.com/css2?family=Poppins:wght@400;600&family=Tinos&display=swap">
<style>
  :root {
    --page: #ffffff;
    --navy-light: #13233d;
    --navy: #0a1629;
    --navy-deep: #040c1b;
    --gold: #f4a93c;
    --gold-deep: #8a5a12;
    --white: #ffffff;
    --line-blue: #2a3f63;
    --scene-blue: #1d2f4f;
    --shadow: rgba(0, 0, 0, 0.45);
  }
  * { box-sizing: border-box; margin: 0; padding: 0; }
  html, body { width: 944px; height: 1200px; overflow: hidden; background: var(--page); }
  .canvas { position: relative; width: 944px; height: 1200px; }

  .card {
    position: absolute;
    left: 121px;
    width: 702px;
    height: 401px;
    overflow: hidden;
    background: linear-gradient(135deg, var(--navy-light) 0%, var(--navy) 40%, var(--navy-deep) 100%);
    box-shadow: 14px 22px 28px var(--shadow);
  }
  .card--front { top: 160px; }
  .card--back { top: 639px; }

  .wordmark {
    position: absolute;
    display: flex;
    align-items: center;
    gap: 12px;
    font-family: "Poppins", sans-serif;
    font-weight: 600;
    color: var(--white);
    white-space: nowrap;
    z-index: 2;
  }
  .wordmark__dot {
    display: block;
    border-radius: 50%;
    background: var(--gold);
  }
  .card--front .wordmark { left: 0; right: 0; justify-content: center; top: 98px; font-size: 40px; }
  .card--front .wordmark__dot { width: 26px; height: 26px; }
  .card--back .wordmark { left: 53px; top: 76px; font-size: 30px; }
  .card--back .wordmark__dot { width: 20px; height: 20px; }

  .terrain {
    position: absolute;
    left: 0; right: 0; bottom: 0;
    height: 171px;
    background:
      radial-gradient(ellipse at 60% 60%, rgba(244, 169, 60, 0.55), transparent 65%),
      linear-gradient(180deg, rgba(138, 90, 18, 0) 0%, var(--gold-deep) 45%, #b07a22 100%);
  }

  .holder {
    position: absolute;
    left: 53px;
    top: 182px;
    font-family: "Tinos", serif;
    font-weight: 400;
    font-size: 35px;
    line-height: 1.2;
    color: var(--gold);
    white-space: nowrap;
    z-index: 2;
  }
  .holder-rule {
    position: absolute;
    left: 53px;
    top: 239px;
    width: 75px;
    height: 2px;
    background: var(--gold);
  }
  .contact {
    position: absolute;
    left: 53px;
    top: 264px;
    list-style: none;
    font-family: "Poppins", sans-serif;
    font-size: 17px;
    color: var(--white);
    z-index: 2;
  }
  .contact__item { display: flex; align-items: center; gap: 8px; height: 26px; margin-bottom: 8px; }
  .contact__icon { width: 24px; height: 24px; flex: none; }

  .base-lines {
    position: absolute;
    left: 0;
    top: 372px;
    width: 702px;
    height: 22px;
    border-top: 2px solid var(--line-blue);
    border-bottom: 2px solid var(--line-blue);
    z-index: 1;
  }

  .landmark {
    position: absolute;
    left: 360px;
    top: 140px;
    width: 342px;
    height: 261px;
    background:
      radial-gradient(circle at 70% 30%, rgba(244, 169, 60, 0.85) 0%, rgba(244, 169, 60, 0.5) 9%, rgba(244, 169, 60, 0) 20%),
      radial-gradient(ellipse at 62% 85%, var(--scene-blue) 0%, rgba(29, 47, 79, 0.7) 40%, rgba(29, 47, 79, 0) 75%);
    -webkit-mask-image: linear-gradient(90deg, transparent 0%, #000 30%);
    mask-image: linear-gradient(90deg, transparent 0%, #000 30%);
  }
</style>
</head>
<body>
<main class="canvas">

  <section class="card card--front" aria-label="Card front">
    <div class="wordmark">Pellrow Strategies<span class="wordmark__dot"></span></div>
    <div class="terrain" role="img" aria-label="Glowing gold topographic contour lines across the lower half of the card"></div>
  </section>

  <section class="card card--back" aria-label="Card back">
    <div class="wordmark">Pellrow Strategies<span class="wordmark__dot"></span></div>

    <h1 class="holder">Colin Mabberly</h1>
    <div class="holder-rule"></div>

    <ul class="contact">
      <li class="contact__item">
        <svg class="contact__icon" viewBox="0 0 24 24" aria-hidden="true">
          <circle cx="12" cy="12" r="11" fill="none" stroke="var(--gold)" stroke-width="1.5"/>
          <rect x="7" y="8.5" width="10" height="7" rx="1" fill="var(--gold)"/>
          <path d="M7.3 9 L12 12.6 L16.7 9" fill="none" stroke="var(--navy)" stroke-width="1"/>
        </svg>
        <span>colin@pellrowstrategies.example</span>
      </li>
      <li class="contact__item">
        <svg class="contact__icon" viewBox="0 0 24 24" aria-hidden="true">
          <circle cx="12" cy="12" r="11" fill="none" stroke="var(--gold)" stroke-width="1.5"/>
          <path d="M8.5 7.5 l2 0 l0.8 2.4 l-1.3 1 a6 6 0 0 0 3.1 3.1 l1 -1.3 l2.4 0.8 l0 2 a1 1 0 0 1 -1 1 a8.5 8.5 0 0 1 -8 -8 a1 1 0 0 1 1 -1z" fill="var(--gold)"/>
        </svg>
        <span>202-555-0148</span>
      </li>
    </ul>

    <div class="landmark" role="img" aria-label="Line illustration of a capitol dome before mountains with a rising gold sun"></div>
    <div class="base-lines"></div>
  </section>

</main>
</body>
</html>
```